We are having a Bright Dawn, Bold Self Reshape Challenge at our fitness studio. We need a poster design using the template attached as a reference. I have also included our Vorabloom logo to put on the poster. Please DO NOT use the graphics in the flyer as we are expecting something much better :-)

-Size needed 11x17 with bleeding for printing

-We need this made in Photoshop (CS3 friendly) or at least delivered in PS as we might change some text or re-arrange the design later on.

-We need this in layers.

```html
<!DOCTYPE html>
<html lang="en">
<head>
<meta charset="utf-8">
<title>Bright Dawn, Bold Self Reshape Challenge</title>
<link rel="stylesheet" href="https://fonts.googleapis.com/css2?family=Passion+One:wght@400;700&family=Open+Sans:ital,wght@0,700;0,800;1,700&display=swap">
<style>
  :root {
    --bg-warm: #c4652c;
    --bg-mid: #8a5a6e;
    --bg-cool: #4a4f9e;
    --red: #e3202a;
    --yellow: #ffe600;
    --white: #ffffff;
    --ice: #cfe2f5;
    --silhouette-light: #e6e2ea;
    --silhouette-dark: #b9b2c6;
  }
  * { margin: 0; padding: 0; box-sizing: border-box; }
  html, body { width: 778px; height: 1200px; overflow: hidden; }
  body { font-family: "Open Sans", Arial, sans-serif; }

  .poster {
    position: relative;
    width: 778px;
    height: 1200px;
    overflow: hidden;
    background: linear-gradient(100deg, var(--bg-warm) 0%, var(--bg-mid) 50%, var(--bg-cool) 100%);
  }

  .athlete-figure {
    position: absolute;
    left: 60px;
    top: 90px;
    width: 330px;
    height: 1110px;
    border-radius: 160px 160px 40px 40px;
    background: linear-gradient(180deg, var(--silhouette-light), var(--silhouette-dark));
    opacity: 0.5;
  }

  .brand {
    position: absolute;
    left: 22px;
    top: 30px;
    display: flex;
    align-items: center;
    gap: 14px;
  }
  .brand-mark {
    width: 34px;
    height: 34px;
    background: var(--white);
  }
  .brand-name {
    font-family: "Passion One", Impact, sans-serif;
    font-weight: 700;
    font-size: 60px;
    line-height: 1;
    color: var(--white);
    letter-spacing: 1px;
  }

  .headline {
    position: absolute;
    left: 320px;
    top: 148px;
    width: 450px;
    text-align: center;
    font-family: "Passion One", Impact, sans-serif;
    font-weight: 700;
    font-size: 68px;
    line-height: 72px;
    color: var(--red);
    -webkit-text-stroke: 6px var(--white);
    paint-order: stroke fill;
    text-transform: uppercase;
  }
  .headline span { display: block; }

  .tagline {
    position: absolute;
    left: 450px;
    top: 462px;
    width: 320px;
    text-align: center;
    color: var(--white);
    font-weight: 800;
    font-size: 23px;
    line-height: 1.3;
  }

  .dates {
    position: absolute;
    left: 522px;
    top: 648px;
    width: 250px;
    padding: 12px 12px;
    background: var(--red);
    color: var(--white);
    font-size: 15px;
    font-weight: 700;
    line-height: 1.3;
  }
  .dates dt { color: var(--yellow); font-style: italic; }
  .dates dd { margin-bottom: 10px; white-space: nowrap; }
  .dates dd:last-child { margin-bottom: 0; }

  .program-weeks {
    position: absolute;
    left: 62px;
    top: 612px;
    font-family: "Passion One", Impact, sans-serif;
    font-size: 170px;
    line-height: 1;
    color: transparent;
    -webkit-text-stroke: 3px var(--ice);
  }
  .program-copy {
    position: absolute;
    left: 40px;
    top: 772px;
    width: 400px;
    color: var(--ice);
    font-size: 22px;
    font-weight: 700;
    line-height: 1.3;
  }
  .program-price {
    position: absolute;
    left: 74px;
    top: 850px;
    font-family: "Passion One", Impact, sans-serif;
    font-size: 190px;
    line-height: 1;
    color: transparent;
    -webkit-text-stroke: 3px var(--ice);
  }

  .prize {
    position: absolute;
    left: 596px;
    top: 945px;
    width: 156px;
    height: 156px;
    border-radius: 50%;
    background: var(--red);
    border: 3px solid var(--white);
    display: flex;
    flex-direction: column;
    align-items: center;
    justify-content: center;
    text-align: center;
    color: var(--yellow);
    font-weight: 800;
    font-size: 19px;
    line-height: 1.15;
  }

  .footer {
    position: absolute;
    left: 0;
    bottom: 6px;
    width: 778px;
    height: 40px;
    background: var(--red);
    color: var(--white);
    font-weight: 800;
    font-size: 18px;
    display: flex;
    align-items: center;
    justify-content: center;
    gap: 8px;
  }
  .footer .url { color: var(--yellow); }
</style>
</head>
<body>
<main class="poster">
  <div class="athlete-figure" role="img" aria-label="Silhouette of a woman lifting a dumbbell"></div>

  <div class="brand">
    <span class="brand-mark"></span>
    <span class="brand-name">VORABLOOM</span>
  </div>

  <h1 class="headline">
    <span>Bright Dawn,</span>
    <span>Bold Self</span>
    <span>Reshape</span>
    <span>Challenge</span>
  </h1>

  <p class="tagline">In Just 6 Weeks, Transform Your Body And Get In The Best Shape Of Your Life!</p>

  <dl class="dates">
    <dt>Kick Off Meeting:</dt>
    <dd>Thursday, Jan 14 at 7:30 pm</dd>
    <dt>Start Date:</dt>
    <dd>Monday, January 18th</dd>
    <dt>End Date:</dt>
    <dd>Friday, February 26th</dd>
  </dl>

  <div class="program-weeks">6</div>
  <p class="program-copy">Weeks of Training, Nutrition, and Coaching Starting at just</p>
  <div class="program-price">$99!</div>

  <div class="prize">
    <span>$500</span>
    <span>CASH Prize</span>
    <span>for Winner!</span>
  </div>

  <footer class="footer">
    <span>Visit</span><span class="url">www.vorabloombootcamps.com</span><span>FOR MORE INFO</span>
  </footer>
</main>
</body>
</html>
```